METAL FABRICATION BUSINESS CARD

** I will be ending the project and picking design early. This Friday October 3rd at 7am MST if not sooner**
ONE SIDED BUSINESS CARD ONLY. AND LOGO SIZE TO BE DOMINANT so it stands out.
Looking for a black background and will be doing raised chrome/silver font on the business cards. Looking to have the following on the front of the business card. Company logo is uploaded in files.
Company logo
*Compartment Doors
*Roof Radius Metal
*J-Wrap Metal Skirting
*S-Lock Beltline Molding
*Pre-Bent Molding
and more...
Owen Daltry 307.552.4198 info@KX-Welt.com
Updates
One sided business card only please. Also logo size should be dominant and sized bigger
Contact Information for Business Card
Black background, Text will be raised chrome/silver, and corners will be rounded.

```html
<!DOCTYPE html>
<html lang="en">
<head>
<meta charset="utf-8">
<title>KX-Welt Business Card</title>
<link rel="stylesheet" href="https://fonts.googleapis.com/css2?family=Archivo+Black&family=Lato:wght@400;700&display=swap">
<style>
  :root {
    --stage: #1c1c1c;
    --card: #0b0b0b;
    --chrome: #cfcfcf;
    --chrome-light: #f2f2f2;
    --chrome-dark: #8d8d8d;
    --ink: #1a1a1a;
    --text-silver: #dcdcdc;
  }
  * { margin: 0; padding: 0; box-sizing: border-box; }
  html, body { width: 1200px; height: 923px; overflow: hidden; background: var(--stage); }
  .canvas { position: relative; width: 1200px; height: 923px; }
  .card {
    position: absolute; left: 150px; top: 204px; width: 900px; height: 514px;
    background: var(--card); border-radius: 26px; overflow: hidden;
  }
  .card-shapes { position: absolute; inset: 0; }
  .brand {
    position: absolute; left: 96px; top: 52px;
    display: flex; align-items: center; gap: 22px;
  }
  .brand-dot { width: 46px; height: 46px; border-radius: 50%; background: var(--chrome); }
  .brand-name {
    font-family: "Archivo Black", sans-serif; font-size: 132px; line-height: 1;
    color: var(--chrome); letter-spacing: 1px;
  }
  .services {
    position: absolute; left: 556px; top: 258px; list-style: none;
    font-family: "Lato", sans-serif; font-size: 21px; line-height: 31px;
    color: var(--ink); letter-spacing: 0.5px; text-transform: uppercase;
  }
  .services li { display: flex; align-items: center; gap: 10px; }
  .services .tick { width: 16px; height: 16px; flex: none; }
  .services .more { padding-left: 26px; }
  .contact {
    position: absolute; left: 150px; top: 350px; font-family: "Lato", sans-serif;
    color: var(--text-silver);
  }
  .contact-name {
    font-family: "Archivo Black", sans-serif; font-size: 30px; letter-spacing: 2px;
    text-transform: uppercase; color: var(--chrome); margin-bottom: 10px;
  }
  .contact-line { display: flex; align-items: center; gap: 14px; font-size: 25px; line-height: 40px; }
  .contact-line svg { width: 18px; height: 18px; flex: none; }
  .phone { font-weight: 700; }
</style>
</head>
<body>
<div class="canvas">
  <div class="card">
    <svg class="card-shapes" viewBox="0 0 900 514" aria-hidden="true">
      <defs>
        <linearGradient id="chrome" x1="0" y1="0" x2="1" y2="1">
          <stop offset="0" stop-color="var(--chrome-dark)"/>
          <stop offset="0.35" stop-color="var(--chrome-light)"/>
          <stop offset="0.7" stop-color="var(--chrome)"/>
          <stop offset="1" stop-color="var(--chrome-light)"/>
        </linearGradient>
      </defs>
      <polygon class="service-panel" points="548,222 900,222 900,514 520,514" fill="url(#chrome)"/>
      <polygon class="corner-fold" points="0,372 88,372 130,514 0,514" fill="url(#chrome)"/>
    </svg>

    <div class="brand">
      <span class="brand-dot"></span>
      <span class="brand-name">KX-Welt</span>
    </div>

    <ul class="services">
      <li><svg class="tick" viewBox="0 0 16 16"><circle cx="8" cy="8" r="8" fill="#1a1a1a"/><path d="M4.5 8.3l2.3 2.2 4.7-4.8" stroke="#fff" stroke-width="1.8" fill="none"/></svg>Compartment Doors</li>
      <li><svg class="tick" viewBox="0 0 16 16"><circle cx="8" cy="8" r="8" fill="#1a1a1a"/><path d="M4.5 8.3l2.3 2.2 4.7-4.8" stroke="#fff" stroke-width="1.8" fill="none"/></svg>Roof Radius Metal</li>
      <li><svg class="tick" viewBox="0 0 16 16"><circle cx="8" cy="8" r="8" fill="#1a1a1a"/><path d="M4.5 8.3l2.3 2.2 4.7-4.8" stroke="#fff" stroke-width="1.8" fill="none"/></svg>J-Wrap Metal Skirting</li>
      <li><svg class="tick" viewBox="0 0 16 16"><circle cx="8" cy="8" r="8" fill="#1a1a1a"/><path d="M4.5 8.3l2.3 2.2 4.7-4.8" stroke="#fff" stroke-width="1.8" fill="none"/></svg>S-Lock Beltline Molding</li>
      <li><svg class="tick" viewBox="0 0 16 16"><circle cx="8" cy="8" r="8" fill="#1a1a1a"/><path d="M4.5 8.3l2.3 2.2 4.7-4.8" stroke="#fff" stroke-width="1.8" fill="none"/></svg>Pre-Bent Molding</li>
      <li class="more">And more...</li>
    </ul>

    <div class="contact">
      <p class="contact-name">Owen Daltry</p>
      <p class="contact-line phone">
        <svg viewBox="0 0 18 18"><path d="M4 1.5l3 3-1.8 2.2c1 2 2.6 3.6 4.6 4.6L12 9.5l3 3-2 2.7C7.5 15 3 10.5 1.3 4z" fill="var(--text-silver)"/></svg>
        307.552.4198
      </p>
      <p class="contact-line">
        <svg viewBox="0 0 18 18"><rect x="1" y="3.5" width="16" height="11" fill="var(--text-silver)"/><path d="M1 3.5l8 6.5 8-6.5" stroke="#0b0b0b" stroke-width="1.4" fill="none"/></svg>
        info@KX-Welt.com
      </p>
    </div>
  </div>
</div>
</body>
</html>
```